Business Cards and Stationary for telecommunications application
BrightOak Ventures
Business Cards and Stationary for telecommunications application - Telecommunications
Creative Brief
Simple
Louis Merrow
President
20391 Kelvane Court Alderbrook Hills, NV
louis@brightoakventures.com
brightoakventures.com

```html
<!DOCTYPE html>
<html lang="en">
<head>
<meta charset="utf-8">
<title>BrightOak Ventures Business Card</title>
<link href="https://fonts.googleapis.com/css2?family=Open+Sans:wght@300;400;600;700&display=swap" rel="stylesheet">
<style>
  :root {
    --page: #e9e7e4;
    --card-white: #ffffff;
    --ink: #5a5a5a;
    --ink-soft: #8a8a8a;
    --brand-red: #d0141b;
    --deep-red: #8e0a0f;
    --black: #0b0b0b;
    --band-grey: #c9c9c9;
  }
  * { margin: 0; padding: 0; box-sizing: border-box; }
  html, body { width: 1200px; height: 732px; overflow: hidden; background: var(--page); }
  body { font-family: "Open Sans", Arial, sans-serif; color: var(--ink); }
  .stage {
    width: 1200px; height: 732px;
    display: flex; align-items: center; justify-content: center; gap: 50px;
  }
  .card {
    position: relative; width: 530px; height: 303px; overflow: hidden;
    border-radius: 3px; box-shadow: 0 3px 10px rgba(0,0,0,0.18);
  }
  /* Front */
  .card-front { background: var(--card-white); }
  .front-bands { position: absolute; left: 0; bottom: 0; width: 530px; height: 130px; }
  .brand-lockup {
    position: absolute; top: 40px; left: 0; width: 100%;
    display: flex; align-items: center; justify-content: center; gap: 8px;
  }
  .brand-dot { width: 14px; height: 14px; border-radius: 50%; background: var(--brand-red); flex-shrink: 0; }
  .brand-name { font-size: 21px; font-weight: 400; color: var(--brand-red); letter-spacing: -0.3px; white-space: nowrap; }
  .person { position: absolute; top: 108px; left: 34px; }
  .person-name { font-size: 17px; font-weight: 300; color: var(--ink); }
  .person-name strong { font-weight: 700; color: var(--ink); }
  .person-title { font-size: 13px; font-weight: 300; color: var(--ink-soft); margin-top: 1px; }
  .person-address { font-size: 12px; font-weight: 300; color: var(--ink); margin-top: 12px; line-height: 1.35; }
  .contacts { position: absolute; top: 100px; right: 34px; list-style: none; }
  .contacts li {
    display: flex; align-items: center; gap: 7px;
    font-size: 12.5px; font-weight: 300; color: var(--ink); margin-bottom: 5px; white-space: nowrap;
  }
  .contact-icon {
    width: 14px; height: 14px; border-radius: 50%; background: var(--ink);
    display: flex; align-items: center; justify-content: center; flex-shrink: 0;
  }
  /* Back */
  .card-back {
    background: linear-gradient(100deg, var(--black) 0%, var(--black) 30%, var(--deep-red) 62%, var(--brand-red) 100%);
  }
  .back-mark {
    position: absolute; top: 46%; left: 50%; transform: translate(-50%, -50%);
    display: flex; align-items: center; gap: 12px; white-space: nowrap;
  }
  .back-dot { width: 18px; height: 18px; border-radius: 50%; background: var(--brand-red); flex-shrink: 0; }
  .back-name { font-size: 30px; font-weight: 400; color: #ffffff; }
  .back-web {
    position: absolute; left: 38px; bottom: 26px;
    font-size: 13px; font-weight: 600; letter-spacing: 2px; color: var(--brand-red); white-space: nowrap;
  }
</style>
</head>
<body>
<main class="stage">
  <section class="card card-front" aria-label="Business card front">
    <svg class="front-bands" viewBox="0 0 530 130" preserveAspectRatio="none" aria-hidden="true">
      <path d="M0 40 C150 95 330 95 530 10 L530 130 L0 130 Z" fill="var(--band-grey)" opacity="0.45"/>
      <path d="M0 62 C160 112 340 105 530 35 L530 130 L0 130 Z" fill="var(--deep-red)"/>
      <path d="M0 75 C170 120 350 112 530 55 L530 130 L0 130 Z" fill="var(--brand-red)"/>
      <path d="M0 100 C180 130 360 125 530 90 L530 130 L0 130 Z" fill="var(--black)"/>
    </svg>
    <div class="brand-lockup">
      <span class="brand-dot"></span>
      <span class="brand-name">BrightOak Ventures</span>
    </div>
    <div class="person">
      <p class="person-name">Louis <strong>Merrow</strong></p>
      <p class="person-title">President</p>
      <p class="person-address">20391 Kelvane Court<br>Alderbrook Hills, NV</p>
    </div>
    <ul class="contacts">
      <li><span class="contact-icon"><svg width="8" height="8" viewBox="0 0 10 10"><path d="M2 1 L4 1 L5 3 L4 4 C4.6 5.4 5.6 6.3 6 6 L7 5 L9 6 L9 8 C6 9.5 0.5 4 2 1 Z" fill="#fff"/></svg></span>555-014-2290</li>
      <li><span class="contact-icon"><svg width="8" height="8" viewBox="0 0 10 10"><rect x="1" y="2.5" width="8" height="5" fill="none" stroke="#fff"/><path d="M1 2.5 L5 6 L9 2.5" fill="none" stroke="#fff"/></svg></span>louis@brightoakventures.com</li>
      <li><span class="contact-icon"><svg width="8" height="8" viewBox="0 0 10 10"><circle cx="5" cy="5" r="3.8" fill="none" stroke="#fff"/><path d="M1.2 5 H8.8 M5 1.2 V8.8" stroke="#fff"/></svg></span>www.brightoakventures.com</li>
    </ul>
  </section>

  <section class="card card-back" aria-label="Business card back">
    <div class="back-mark">
      <span class="back-dot"></span>
      <span class="back-name">BrightOak Ventures</span>
    </div>
    <p class="back-web">www.brightoakventures.com</p>
  </section>
</main>
</body>
</html>
```